Radiant Harvest Gathering 2021

I am looking to create a flyer for a one day prayer retreat our church is organizing. This flyer will be posted on social media, websites, mobile apps, and will also be printed so it can be mailed to people.

I am looking for something professional, with good use of our logo and band colors (logo colors).

I am counting on the designer's skill, creativity, art and knowledge of media communication to produce a flyer that will effectively and quickly convey the message we are trying to spread.

CONTENT OF THE FLYER:
Event title: Radiant Harvest Gathering
Date: Tuesday July 2nd, 2021
Time: 11:00AM - 7:00PM
Bellmore Hotel, 4817 Wexley Avenue, Portland, Maine 04109 (Room: Tamarind)
Event Key words to highlight what the event is about: Prayer, Fasting, Worship, Prophecy, Revival.
Key phrases:
A one day prayer retreat.
Jesus Chris is Lord

Contact info:
www.quvello.org
Phone: 207 555 0148
Email: contact@brookmeadow.org

```html
<!DOCTYPE html>
<html lang="en">
<head>
<meta charset="utf-8">
<title>Radiant Harvest Gathering 2021</title>
<link rel="stylesheet" href="https://fonts.googleapis.com/css2?family=Cinzel:wght@400;500;600;700&family=Montserrat:wght@500;600;700;800&display=swap">
<style>
  :root {
    --navy: #063a5f;
    --navy-deep: #042c49;
    --orange: #f5931f;
    --white: #ffffff;
    --photo-mid: #5d7690;
    --photo-light: #9aa9b5;
    --photo-warm: #8a6a55;
  }
  * { box-sizing: border-box; margin: 0; padding: 0; }
  html, body { width: 990px; height: 1200px; overflow: hidden; background: var(--navy); }
  .flyer {
    position: relative; width: 990px; height: 1200px; overflow: hidden;
    background: var(--navy); font-family: "Montserrat", sans-serif; color: var(--white);
  }
  .photo-area {
    position: absolute; left: 0; top: 150px; width: 990px; height: 580px;
    background:
      radial-gradient(ellipse 45% 40% at 52% 45%, var(--photo-light) 0%, rgba(93,118,144,0.6) 45%, transparent 80%),
      radial-gradient(ellipse 30% 35% at 25% 55%, rgba(138,106,85,0.55) 0%, transparent 75%),
      radial-gradient(ellipse 35% 30% at 80% 40%, rgba(154,169,181,0.5) 0%, transparent 75%),
      linear-gradient(180deg, var(--navy) 0%, #2c4a66 25%, #35526d 60%, var(--navy) 100%);
  }
  .title {
    position: absolute; left: 0; width: 990px; text-align: center;
    font-family: "Cinzel", serif; font-weight: 500; color: var(--orange);
    top: 58px; font-size: 74px; line-height: 1; letter-spacing: 1px;
  }
  .title-band {
    position: absolute; left: 99px; top: 144px; width: 793px; height: 84px;
    background: var(--orange); display: flex; align-items: center; justify-content: center;
    font-family: "Cinzel", serif; font-weight: 500; font-size: 68px; color: var(--white); line-height: 1;
    padding-top: 4px;
  }
  .tagline {
    position: absolute; left: 0; width: 990px; top: 242px; text-align: center;
    font-family: "Cinzel", serif; font-weight: 500; color: var(--orange);
    font-size: 26px; letter-spacing: 9px;
  }
  .date-icon { position: absolute; left: 118px; top: 686px; width: 76px; height: 76px; }
  .date-divider { position: absolute; left: 219px; top: 676px; width: 2px; height: 86px; background: var(--white); }
  .date-day { position: absolute; left: 243px; top: 678px; font-size: 45px; font-weight: 800; line-height: 1; }
  .date-full { position: absolute; left: 243px; top: 728px; font-size: 30px; font-weight: 700; line-height: 1; }
  .time-pill {
    position: absolute; left: 116px; top: 782px; width: 381px; height: 46px;
    background: var(--orange); border-radius: 23px; display: flex; align-items: center;
    padding-left: 25px; gap: 16px; font-size: 29px; font-weight: 700;
  }
  .time-pill svg { width: 32px; height: 32px; }
  .venue {
    position: absolute; left: 565px; top: 696px; width: 308px; height: 132px;
    border: 1.5px solid var(--orange); border-radius: 4px; text-align: center;
    padding-top: 20px; font-size: 17px; font-weight: 700; line-height: 26px;
  }
  .venue-pin {
    position: absolute; left: 697px; top: 666px; width: 44px; height: 38px;
    background: var(--navy); display: flex; justify-content: center;
  }
  .venue-room { color: var(--orange); font-weight: 500; font-size: 15.5px; margin-top: 3px; }
  .keywords-frame {
    position: absolute; left: 112px; top: 861px; width: 766px; height: 92px;
    border: 1.5px solid var(--white); border-radius: 4px;
  }
  .keywords-gap {
    position: absolute; left: 220px; top: 940px; width: 550px; height: 20px; background: var(--navy);
  }
  .keywords {
    position: absolute; left: 0; width: 990px; text-align: center;
    font-family: "Cinzel", serif; font-weight: 600; color: var(--orange); font-size: 47px; line-height: 54px;
    top: 872px;
  }
  .brand {
    position: absolute; left: 240px; top: 1035px; transform: translateX(-50%);
    display: flex; align-items: center; gap: 14px;
  }
  .brand-dot { width: 30px; height: 30px; border-radius: 50%; background: var(--orange); }
  .brand-name { font-family: "Cinzel", serif; font-weight: 500; font-size: 64px; color: var(--white); line-height: 1; }
  .contact-divider { position: absolute; left: 494px; top: 1041px; width: 2px; height: 110px; background: var(--white); }
  .phone-pill {
    position: absolute; left: 596px; top: 1048px; width: 294px; height: 34px;
    background: var(--orange); border-radius: 17px; font-size: 27px; font-weight: 700;
    line-height: 34px; padding-left: 24px;
  }
  .phone-icon { position: absolute; left: 576px; top: 1046px; width: 38px; height: 38px; }
  .contact-line {
    position: absolute; left: 580px; display: flex; align-items: center; gap: 14px;
    font-size: 20.5px; font-weight: 500;
  }
  .contact-line svg { width: 18px; height: 18px; }
  .web { top: 1093px; }
  .mail { top: 1124px; }
</style>
</head>
<body>
<main class="flyer">
  <div class="photo-area" role="img" aria-label="Photograph of several hands joined together in prayer over open Bibles"></div>

  <h1 class="title">RADIANT HARVEST</h1>
  <div class="title-band">GATHERING</div>
  <p class="tagline">A ONE DAY PRAYER RETREAT.</p>

  <svg class="date-icon" viewBox="0 0 76 76" fill="none" stroke="var(--orange)" stroke-width="4">
    <rect x="3" y="12" width="70" height="60" rx="6"/>
    <line x1="3" y1="27" x2="73" y2="27"/>
    <line x1="20" y1="4" x2="20" y2="18" stroke-linecap="round"/>
    <line x1="56" y1="4" x2="56" y2="18" stroke-linecap="round"/>
    <g stroke-width="5" stroke-linecap="round">
      <line x1="15" y1="39" x2="23" y2="39"/><line x1="34" y1="39" x2="42" y2="39"/><line x1="53" y1="39" x2="61" y2="39"/>
      <line x1="15" y1="50" x2="23" y2="50"/><line x1="34" y1="50" x2="42" y2="50"/><line x1="53" y1="50" x2="61" y2="50"/>
      <line x1="15" y1="61" x2="23" y2="61"/><line x1="34" y1="61" x2="42" y2="61"/><line x1="53" y1="61" x2="61" y2="61"/>
    </g>
  </svg>
  <div class="date-divider"></div>
  <div class="date-day">TUESDAY</div>
  <div class="date-full">JULY 2ND, 2021</div>

  <div class="time-pill">
    <svg viewBox="0 0 32 32" fill="none" stroke="var(--white)" stroke-width="1.6">
      <circle cx="16" cy="16" r="14"/><circle cx="16" cy="16" r="10.5"/>
      <polyline points="16,9 16,16 20,19" stroke-linecap="round"/>
    </svg>
    <span>11:00AM - 7:00PM</span>
  </div>

  <div class="venue">
    Bellmore Hotel,<br>4817 Wexley Avenue,<br>Portland, Maine 04109
    <div class="venue-room">(Room: Tamarind)</div>
  </div>
  <div class="venue-pin">
    <svg width="26" height="34" viewBox="0 0 26 34" fill="none" stroke="var(--orange)" stroke-width="3">
      <path d="M13 24 C7 16 5 13 5 10 A8 8 0 0 1 21 10 C21 13 19 16 13 24 Z"/>
      <circle cx="13" cy="10" r="3"/>
      <path d="M5 28 Q13 33 21 28" stroke-linecap="round"/>
    </svg>
  </div>

  <div class="keywords-frame"></div>
  <div class="keywords-gap"></div>
  <p class="keywords">Prayer, Fasting, Worship,<br>Prophecy, Revival.</p>

  <div class="brand">
    <span class="brand-dot"></span>
    <span class="brand-name">Quvello</span>
  </div>

  <div class="contact-divider"></div>
  <div class="phone-pill">207 555 0148</div>
  <svg class="phone-icon" viewBox="0 0 38 38">
    <circle cx="19" cy="19" r="17" fill="var(--navy)" stroke="var(--white)" stroke-width="2.5"/>
    <path d="M13 10 l4 0 l1.5 5 l-2.5 2 q2 4 5.5 5.5 l2-2.5 l5 1.5 l0 4 q-1 2-4 2 q-12-2-14-14 q0-3 2.5-3.5z" fill="var(--white)"/>
  </svg>
  <div class="contact-line web">
    <svg viewBox="0 0 18 18" fill="none" stroke="var(--orange)" stroke-width="1.4">
      <circle cx="9" cy="9" r="7.5"/><ellipse cx="9" cy="9" rx="3.5" ry="7.5"/>
      <line x1="1.5" y1="9" x2="16.5" y2="9"/><line x1="3" y1="5" x2="15" y2="5"/><line x1="3" y1="13" x2="15" y2="13"/>
    </svg>
    <span>www.quvello.org</span>
  </div>
  <div class="contact-line mail">
    <svg viewBox="0 0 18 18" fill="none" stroke="var(--orange)" stroke-width="1.4">
      <rect x="1.5" y="4" width="15" height="10"/><polyline points="1.5,4 9,10 16.5,4"/>
    </svg>
    <span>contact@brookmeadow.org</span>
  </div>
</main>
</body>
</html>
```